Label design for Japanese healthy drink

We need new label design to give our product a new look. This is Amazake, traditional Japanese drink made out of fermented rice. This is nutrition packed drink and target audience is health conscious people. We want something simple and healthy. The attached photo is current label (for the size reference only) and food pouch the label will be attached. Please don't use anything on the label in the picture.

Target Market(s)

health conscious people (30s - 50s)

Requirements
Must have
• "Amazake"
Should not have
• too much color, picture of rice or sake

```html
<!DOCTYPE html>
<html lang="en">
<head>
<meta charset="UTF-8">
<title>Amazake Label Designs</title>
<link rel="stylesheet" href="https://fonts.googleapis.com/css2?family=Open+Sans:wght@400;600;700&family=Noto+Sans+JP:wght@400;700&display=swap">
<style>
  :root {
    --page: #ffffff;
    --night: #000000;
    --leaf: #6dbb3f;
    --snow: #ffffff;
    --leaf-grey: #4a4a4a;
    --cream: #f3e4c8;
    --cocoa: #4a3b2c;
    --honey: #e9b94c;
    --grain-gold: #e8b84a;
  }
  * { margin: 0; padding: 0; box-sizing: border-box; }
  html, body {
    width: 1200px;
    height: 1200px;
    overflow: hidden;
    background: var(--page);
  }
  .board {
    position: relative;
    width: 1200px;
    height: 1200px;
  }
  .label {
    position: absolute;
    top: 352px;
    width: 520px;
    height: 496px;
    font-family: "Open Sans", sans-serif;
  }
  .label--night { left: 70px; background: var(--night); color: var(--snow); }
  .label--cream { left: 610px; background: var(--cream); color: var(--cocoa); }

  .label__frame {
    position: absolute;
    inset: 22px;
    border: 2px solid var(--leaf);
  }
  .label--cream .label__frame { border-color: var(--cocoa); }

  .label__organic {
    position: absolute;
    top: 88px;
    left: 0; right: 0;
    text-align: center;
    font-size: 16px;
    font-weight: 600;
    letter-spacing: 3px;
  }
  .label__title {
    position: absolute;
    top: 104px;
    left: 0; right: 0;
    text-align: center;
    font-size: 72px;
    font-weight: 700;
    letter-spacing: 1px;
    line-height: 1.1;
  }
  .label--night .label__title { color: var(--leaf); }

  .label__subtitle {
    position: absolute;
    top: 210px;
    left: 0; right: 0;
    text-align: center;
    font-size: 18px;
    letter-spacing: 0.8px;
  }
  .label--cream .label__subtitle {
    left: 50%;
    right: auto;
    transform: translateX(-50%);
    width: 424px;
    padding: 2px 0;
    background: var(--honey);
  }

  .label__rule {
    position: absolute;
    top: 275px;
    left: 50px;
    width: 420px;
    height: 5px;
    background: var(--leaf);
  }

  .label__tagline {
    position: absolute;
    top: 344px;
    left: 64px;
    font-family: "Noto Sans JP", sans-serif;
    font-size: 34px;
    font-weight: 400;
  }
  .label--cream .label__tagline {
    top: 298px;
    left: 40px;
    font-weight: 700;
    font-size: 38px;
  }

  .label__weight {
    position: absolute;
    top: 438px;
    left: 218px;
    font-size: 15px;
  }

  .label__grain {
    position: absolute;
    top: 330px;
    left: 394px;
    width: 88px;
    height: 140px;
  }
  .label--cream .label__grain { top: 330px; left: 394px; }
</style>
</head>
<body>
<main class="board">

  <section class="label label--night">
    <div class="label__frame"></div>
    <p class="label__organic">ORGANIC</p>
    <h1 class="label__title">AMAZAKE</h1>
    <p class="label__subtitle">JAPANESE FERMENTED RICE DRINK</p>
    <div class="label__rule"></div>
    <p class="label__tagline">これも、Oh! こめ</p>
    <p class="label__weight">250grams</p>
    <svg class="label__grain" viewBox="0 0 88 140" role="img" aria-label="Two grain ear illustrations in dark grey">
      <rect x="0" y="0" width="88" height="140" rx="30" fill="var(--leaf-grey)"/>
    </svg>
  </section>

  <section class="label label--cream">
    <div class="label__frame"></div>
    <p class="label__organic">ORGANIC</p>
    <h1 class="label__title">AMAZAKE</h1>
    <p class="label__subtitle">JAPANESE FERMENTED RICE DRINK</p>
    <p class="label__tagline">これも、Oh! こめ</p>
    <p class="label__weight">250grams</p>
    <svg class="label__grain" viewBox="0 0 88 140" role="img" aria-label="Two grain ear illustrations in golden yellow">
      <rect x="0" y="0" width="88" height="140" rx="30" fill="var(--grain-gold)"/>
    </svg>
  </section>

</main>
</body>
</html>
```